TELVORA needs three flags/signs to celebrate green buildings

The template for the flag is in the attachments, and can be found on

We are looking to celebrate three of Australia's most energy efficient buildings by creating some signage for them to display. One will be an office building, one a hotel, one a shopping centre. They should include the words: "You are entering Australia's most energy efficient office/hotel/shopping centre".

So to clarify, there will need to be three different designs (office/hotel/shopping centre) but each design will need consider two sides of the flag.
Updates

Thanks to everyone who submitted a design. I have already given feedback to most. I will provide feedback to those I haven't by the end of the day. We received 30 designs all up, over half were good quality and some were very good quality. Today I'll put my favourites through to our wider team for a poll. Many thanks once again.

Target Market(s)

People entering the buildings

Industry/Entity Type

Property Management

Font styles to use
Other font styles liked:
• see logo guidelines

Requirements
Must have
• The TELVORA logo.
• The wording "You are entering Australia's most energy efficient office/hotel/shopping centre."
• It should fit into the 'flapterns' templates provided.
• The designs should refer to the TELVORA logo guidelines for style / font.
• Note: we use a seven pointed star.
Nice to have
• We have two elements that we use frequently: stars and a 'wave'. See examples of documents for ideas.
• The final design should communicate celebration with corporate elegance.

```html
<!DOCTYPE html>
<html lang="en">
<head>
<meta charset="utf-8">
<title>TELVORA – Energy Efficient Building Flags</title>
<link rel="stylesheet" href="https://fonts.googleapis.com/css2?family=Arimo:wght@400;700&display=swap">
<style>
  :root {
    --page: #ffffff;
    --office-light: #7fd0f2;
    --office-mid: #1f8fd6;
    --office-deep: #0b4f9a;
    --hotel-light: #ffd36a;
    --hotel-mid: #f7871f;
    --hotel-deep: #d9480f;
    --retail-light: #2f7fd8;
    --retail-mid: #0d2d6e;
    --retail-deep: #06153a;
    --ink-dark: #0e2346;
    --ink-light: #ffffff;
    --badge-amber: #f0a431;
    --badge-red: #d8363b;
    --icon-dark: #1a2436;
  }
  * { box-sizing: border-box; margin: 0; padding: 0; }
  html, body { width: 784px; height: 1200px; overflow: hidden; background: var(--page); }
  body { position: relative; font-family: "Arimo", Arial, sans-serif; }

  .flag {
    position: absolute;
    top: 14px;
    width: 216px;
    height: 1162px;
    overflow: hidden;
    border: 1px solid rgba(0,0,0,0.12);
  }
  .flag--office { left: 34px; }
  .flag--hotel { left: 284px; }
  .flag--retail { left: 534px; }

  .flag__backdrop { position: absolute; inset: 0; }
  .flag--office .flag__backdrop {
    background:
      radial-gradient(ellipse 140% 40% at 30% 28%, rgba(255,255,255,0.55), transparent 60%),
      radial-gradient(ellipse 120% 30% at 80% 78%, rgba(255,255,255,0.4), transparent 65%),
      linear-gradient(180deg, var(--office-mid) 0%, var(--office-light) 40%, var(--office-light) 60%, var(--office-mid) 82%, var(--office-deep) 100%);
  }
  .flag--hotel .flag__backdrop {
    background:
      radial-gradient(circle at 48% 16%, rgba(255,255,230,0.95), transparent 30%),
      radial-gradient(ellipse 130% 30% at 50% 82%, rgba(255,220,120,0.55), transparent 65%),
      linear-gradient(180deg, var(--hotel-mid) 0%, var(--hotel-light) 40%, var(--hotel-mid) 70%, var(--hotel-deep) 100%);
  }
  .flag--retail .flag__backdrop {
    background:
      radial-gradient(ellipse 110% 25% at 60% 30%, rgba(90,180,255,0.6), transparent 65%),
      radial-gradient(ellipse 130% 30% at 40% 80%, rgba(70,160,255,0.55), transparent 65%),
      linear-gradient(180deg, var(--retail-mid) 0%, var(--retail-deep) 35%, var(--retail-mid) 60%, var(--retail-light) 85%, var(--retail-mid) 100%);
  }

  .flag__arc { position: absolute; top: 0; left: 0; width: 216px; height: 380px; }

  .flag__badge { position: absolute; top: 374px; left: 66px; width: 84px; height: 84px; }

  .flag__message {
    position: absolute;
    top: 568px;
    left: 24px;
    font-size: 27px;
    line-height: 47px;
    color: var(--ink-dark);
    letter-spacing: -0.2px;
  }
  .flag__message strong { font-weight: 700; display: block; }
  .flag__message span { display: block; }
  .flag--retail .flag__message { color: var(--ink-light); }

  .flag__brand {
    position: absolute;
    bottom: 40px;
    left: 0;
    right: 0;
    display: flex;
    align-items: center;
    justify-content: center;
    gap: 8px;
    color: var(--ink-light);
    font-weight: 700;
    font-size: 22px;
    letter-spacing: 1px;
  }
  .flag__brand-mark { width: 14px; height: 14px; background: var(--ink-light); }
</style>
</head>
<body>

<section class="flag flag--office">
  <div class="flag__backdrop" role="img" aria-label="Flowing light-blue wave of light with soft sparkles"></div>
  <svg class="flag__arc" viewBox="0 0 216 380"><path d="M16 380 C 20 170, 100 40, 212 4" fill="none" stroke="#1b2a44" stroke-width="1.4"/></svg>
  <svg class="flag__badge" viewBox="0 0 84 84">
    <circle cx="42" cy="42" r="40" fill="var(--badge-amber)"/>
    <rect x="22" y="32" width="40" height="26" rx="3" fill="var(--icon-dark)"/>
    <rect x="34" y="25" width="16" height="9" rx="2" fill="none" stroke="var(--icon-dark)" stroke-width="3"/>
    <rect x="22" y="43" width="40" height="2" fill="var(--badge-amber)"/>
  </svg>
  <p class="flag__message">
    <span>You are</span><strong>entering</strong><strong>Australia's</strong><span>most</span><strong>energy</strong><span>efficient</span><strong>office.</strong>
  </p>
  <div class="flag__brand"><span class="flag__brand-mark"></span>TELVORA</div>
</section>

<section class="flag flag--hotel">
  <div class="flag__backdrop" role="img" aria-label="Warm orange burst of light with glowing bokeh and waves"></div>
  <svg class="flag__arc" viewBox="0 0 216 380"><path d="M16 380 C 20 170, 100 40, 212 4" fill="none" stroke="#3a1c0a" stroke-width="1.4"/></svg>
  <svg class="flag__badge" viewBox="0 0 84 84">
    <circle cx="42" cy="42" r="40" fill="var(--badge-red)"/>
    <path d="M21 52 A21 21 0 0 1 63 52 Z" fill="none" stroke="#fff" stroke-width="3.5"/>
    <circle cx="42" cy="27" r="3" fill="#fff"/>
    <rect x="17" y="54" width="50" height="4" rx="2" fill="#fff"/>
  </svg>
  <p class="flag__message">
    <span>You are</span><strong>entering</strong><strong>Australia's</strong><span>most</span><strong>energy</strong><span>efficient</span><strong>hotel.</strong>
  </p>
  <div class="flag__brand"><span class="flag__brand-mark"></span>TELVORA</div>
</section>

<section class="flag flag--retail">
  <div class="flag__backdrop" role="img" aria-label="Deep navy background with bright blue streaks of light"></div>
  <svg class="flag__arc" viewBox="0 0 216 380"><path d="M16 380 C 20 170, 100 40, 212 4" fill="none" stroke="#cfe3ff" stroke-width="1.4"/></svg>
  <svg class="flag__badge" viewBox="0 0 84 84">
    <circle cx="42" cy="42" r="40" fill="var(--badge-red)"/>
    <path d="M25 34 H59 L56 62 H28 Z" fill="#fff"/>
    <path d="M34 36 V29 A8 8 0 0 1 50 29 V36" fill="none" stroke="#fff" stroke-width="3.5"/>
  </svg>
  <p class="flag__message">
    <span>You are</span><strong>entering</strong><strong>Australia's</strong><span>most</span><strong>energy</strong><span>efficient</span><strong>shoping</strong><strong>centre.</strong>
  </p>
  <div class="flag__brand"><span class="flag__brand-mark"></span>TELVORA</div>
</section>

</body>
</html>
```